Consulting company (stride-and-calm, previously stundenfeld bremen) needs design for a clear and fre

This website is to be made completely new with Worpreess / Divi. I am at the beginning and have no idea about the design. The design is the focus of this order. After the first website I would like to use the design and colors for all other design products for business, which will be placed here as well.
On the website the services, the team, references ... should be separate pages. Please see the attached document. A very important part is the blog and the categories should be visible in the desktop view, vie widgets.

The site should be clear, well-arranged, but still convey freshness and vitality.
Our company offers consulting and online trainings for the following topics:
- Digital paperless office
- process optimization, digitalization
- Remote working and productivity
- Remote leadership
- remote project management
- Time management 4. 0
- Focus on the essentials

We do this in the form of:
- Keynote Speaking
- Facilitating
- Presentation
- Workshops and trainings
- Online trainings

Our services are intended exclusively for companies.

What drives us?
We want to inspire our customers to work more green, lean digital and focus on the essentials. We are a team of three people who are digital nomads, but who also work offline on site.
I do have already webseites, but they are old, but give you an idea what we do: stundenfeld-bremen.example.de. and ms-clearfile.example.com.

One style of a web site I like is for example is that of "plenvika.example.com" Colors I thought so far, but I'm not sure, could be the color palette "quarry bloom" from canva.com or something similar to # f60b80a and # 39dfa7. But I am open for other suggestions.
I love simple and clear fonts. I like this contemporary style of sites, where you get most of the content on the mobile devices by scrolling.

Target Market(s)

midsize and large businesses, decision maker

Logo Text

Let's work Stride and Calm

Number of Pages Required

5+ page

Font styles to use
Sans Serif

Colors
e34297
00a990

Requirements
Must have
• the page should be clear and concise, much white with color accents like content blocks or headlines, responsive,
Nice to have
• I like interesting backgrounds, very discreet, perhaps white and gray or the color shades of pastel, the site should somehow fit to the photos, the logo I added is the old one, just to give you an idea
Should not have
• in no case too playful or loud

```html
<!DOCTYPE html>
<html lang="en">
<head>
<meta charset="utf-8">
<title>Stride and Calm – Consulting</title>
<link href="https://fonts.googleapis.com/css2?family=Poppins:wght@300;400;500;600;700&family=Questrial&family=Arvo:wght@700&family=Roboto+Slab:wght@300;400&display=swap" rel="stylesheet">
<style>
:root{
  --pink:#dc0b78;
  --pink-soft:#ef8fbf;
  --teal:#00a990;
  --ink:#222;
  --muted:#555;
  --dark:#1d1a1e;
  --topbar:#2b1b38;
  --white:#fff;
}
*{box-sizing:border-box;margin:0;padding:0}
html,body{width:1200px;height:4550px;overflow:hidden}
body{position:relative;background:var(--white);font-family:'Poppins',sans-serif;color:var(--ink)}
.abs{position:absolute}
.topbar{left:0;top:0;width:1200px;height:27px;background:var(--topbar);color:#fff;font-size:10px}
.topbar .dots{left:115px;top:5px;display:flex;gap:4px}
.topbar .dots span{width:17px;height:17px;border-radius:50%;background:#fff}
.topbar .contact{right:90px;top:7px;display:flex;gap:22px}
.topbar .contact b{color:var(--pink);font-weight:400;margin-right:4px}
.hero{left:0;top:27px;width:1200px;height:623px;background:linear-gradient(90deg,#eceff1 0%,#dfe3e6 40%,#b9b6b4 70%,#d8d6d4 100%)}
.header{left:0;top:27px;width:1200px;height:58px;background:rgba(255,255,255,.82)}
.logo{left:115px;top:42px;display:flex;align-items:center;gap:8px;font-family:'Poppins',sans-serif;font-weight:600;font-size:19px;color:#3b7a2a}
.logo span.mark{width:26px;height:26px;border-radius:50%;background:#3b7a2a}
.nav{right:110px;top:45px;display:flex;gap:26px;font-size:12px;color:#333}
.hero-text{left:150px;top:170px}
.hero-text .l1{font-family:'Questrial',sans-serif;font-size:50px;line-height:52px;color:#222}
.hero-text .l2{font-family:'Poppins',sans-serif;font-weight:700;font-size:60px;line-height:70px;color:var(--pink);margin-top:4px}
.hero-text .l3{font-size:17px;font-weight:500;letter-spacing:.5px;margin-top:4px}
.btn{display:inline-flex;align-items:center;gap:10px;background:var(--pink);color:#fff;font-size:11px;font-weight:500;padding:0 20px;height:41px;margin-top:22px}
.arrow{width:60px;height:60px;border-radius:50%;background:var(--pink);top:304px}
.section-title{width:1200px;left:0;text-align:center;font-family:'Questrial',sans-serif;font-size:32px;color:#333;letter-spacing:1px}
.section-sub{width:1200px;left:0;text-align:center;font-family:'Roboto Slab',serif;font-size:13px;color:#555;letter-spacing:1px}
.welcome{left:115px;top:782px;width:480px}
.welcome h2{font-family:'Arvo',serif;font-size:28px;color:var(--pink)}
.welcome h3{font-family:'Roboto Slab',serif;font-weight:400;font-size:16px;margin:14px 0 0 3px}
.welcome p{font-size:12.5px;line-height:22px;color:#444;margin:24px 0 0 3px}
.more{font-size:10px;font-weight:500;color:#333;border-bottom:2px solid var(--teal);padding-bottom:2px;display:inline-block;margin-top:24px}
.card{top:1279px;width:215px;height:370px;background:#fff;box-shadow:0 2px 10px rgba(0,0,0,.1);padding:45px 26px 0}
.card.active{top:1255px;height:411px;background:var(--pink);color:#fff;padding-top:69px}
.card h4{font-size:14px;font-weight:600;line-height:18px;color:var(--pink);margin-top:18px;min-height:54px}
.card.active h4,.card.active p,.card.active .rm{color:#fff}
.card p{font-size:10.5px;line-height:18px;color:#444;margin-top:18px}
.card .rm{font-size:10px;font-weight:600;color:var(--pink);border-bottom:1px solid currentColor;display:inline-block;margin-top:28px}
.card .strip{position:absolute;left:0;bottom:0;width:100%;height:18px;background:var(--pink);clip-path:polygon(0 55%,100% 0,100% 100%,0 100%)}
.card.fade{opacity:.55}
.service{top:1853px;width:230px;text-align:center}
.service h5{font-family:'Questrial',sans-serif;font-weight:400;font-size:18px;margin-top:24px}
.service p{font-size:12px;line-height:18px;margin-top:18px;color:#333}
.pager{display:flex;gap:6px}
.pager i{display:block;width:46px;height:4px;background:#222}
.pager i.on{background:var(--pink)}
.quote{top:2248px;width:264px;height:362px;background:#fff;box-shadow:0 2px 12px rgba(0,0,0,.12);text-align:center;padding-top:18px}
.quote.dark{background:#241c1b;color:#fff}
.quote.pink{background:var(--pink);color:#fff}
.quote .avatar{width:58px;height:58px;border-radius:50%;margin:0 auto;background:linear-gradient(#b8c4cf,#5a6a7a)}
.quote .name{font-weight:600;font-size:17px;margin-top:6px}
.quote .co{font-size:10px}
.quote .mk{font-family:'Arvo',serif;font-size:80px;line-height:60px;text-align:left;padding-left:28px;opacity:.25;height:38px;margin-top:10px}
.quote p{font-size:12.5px;line-height:22px;text-align:left;padding:0 28px}
.blog{left:0;top:2757px;width:1200px;height:611px;background:var(--pink)}
.post{top:2891px;width:262px;height:375px;background:#fff;padding:10px 12px}
.post .ph{height:168px;background:linear-gradient(135deg,#cfd8e0,#8a9aaa 60%,#5b6c7e);position:relative}
.post .date{position:absolute;right:8px;top:8px;width:52px;height:46px;background:var(--pink);color:#fff;text-align:center;font-size:16px;font-weight:600;line-height:20px;padding-top:4px}
.post .date small{display:block;font-size:9px;line-height:10px}
.post h4{font-size:14px;font-weight:600;line-height:19px;margin-top:10px;padding:0 4px}
.post p{font-size:10.5px;line-height:18px;margin-top:12px;padding:0 4px}
.post .rm{font-size:11px;font-weight:600;margin-top:18px;padding:0 4px}
.member{top:3545px;width:233px}
.member .ph{height:305px}
.member .n{text-align:center;font-family:'Roboto Slab',serif;font-size:13px;margin-top:12px}
.member .r{text-align:center;font-size:8.5px;color:#555;font-family:'Roboto Slab',serif}
.footer{left:0;top:3950px;width:1200px;height:600px}
.news{left:170px;top:4148px;display:flex;align-items:center;gap:14px;color:#fff;font-family:'Questrial',sans-serif;font-size:22px}
.news .ic{width:40px;height:40px;border-radius:50%;background:var(--pink);display:flex;align-items:center;justify-content:center}
.email{left:480px;top:4147px;width:362px;height:41px;background:#fff;font-size:11px;color:#888;padding:13px 0 0 38px;font-family:'Roboto Slab',serif}
.sub-btn{left:848px;top:4147px;width:148px;height:41px;background:var(--pink);color:#fff;font-size:12px;font-weight:500;text-align:center;line-height:41px}
.fcol{top:4236px;color:#fff;font-size:10.5px;line-height:22px}
.fcol h6{color:var(--pink);font-size:11px;font-weight:600;margin-bottom:10px}
.fcol .arr{color:var(--pink);margin-right:8px}
.rule{left:110px;top:4470px;width:970px;height:1px;background:#3a3538}
.copy{left:110px;top:4503px;color:var(--pink);font-family:'Roboto Slab',serif;font-size:11px}
.follow{right:120px;top:4500px;color:#fff;font-size:11px;font-weight:600;display:flex;gap:6px;align-items:center}
.follow i{width:9px;height:9px;background:var(--teal);display:block}
</style>
</head>
<body>

<div class="abs topbar">
  <div class="abs dots"><span></span><span></span><span></span></div>
  <div class="abs contact"><div><b>✆</b>Phone : 1800 555 0142</div><div><b>✉</b>Mail : hello@strideandcalm.example</div></div>
</div>

<div class="abs hero" role="img" aria-label="Photo of a smiling businesswoman working on a laptop in a bright office"></div>
<div class="abs header"></div>
<div class="abs logo"><span class="mark"></span>Stride and Calm</div>
<nav class="abs nav"><span>Home</span><span>Service</span><span>Testimonials</span><span>Team</span><span>Blog</span><span>Contact Us</span></nav>

<div class="abs hero-text">
  <div class="l1">Making Your<br>Business Ideas</div>
  <div class="l2">Come True</div>
  <div class="l3">RICH AND SUCCESSFUL EXPERIENCE</div>
  <div class="btn">READ MORE
    <svg width="26" height="10" viewBox="0 0 26 10"><path d="M0 5H24M19 1l5 4-5 4" stroke="#fff" fill="none" stroke-width="1.3"/></svg></div>
</div>
<div class="abs arrow" style="left:18px"><svg width="60" height="60"><path d="M34 20l-10 10 10 10" stroke="#fff" fill="none" stroke-width="1.5"/></svg></div>
<div class="abs arrow" style="left:1118px"><svg width="60" height="60"><path d="M26 20l10 10-10 10" stroke="#fff" fill="none" stroke-width="1.5"/></svg></div>

<section class="abs welcome">
  <h2>Welcome to Stride and Calm</h2>
  <h3>When an unknown printer took a galley of type</h3>
  <p>Scrambled it to make a type specimen book. It has survived not only five centuries, but also the leap into electronic typesetting, remaining essentially unchanged. It was popularised in the 1960s with the release of Letraset sheets containing Lorem Ipsum passages, and more re-cently.</p>
  <span class="more">READ MORE</span>
</section>
<div class="abs" style="left:739px;top:738px;width:346px;height:289px;background:var(--pink)"></div>
<div class="abs" style="left:647px;top:792px;width:325px;height:268px;background:linear-gradient(135deg,#d7dde0,#9aa7ad 55%,#2f6b4a)" role="img" aria-label="Photo of a consultant in a green blazer working on a laptop"></div>

<div class="abs section-title" style="top:1122px">Digital paperless office</div>
<div class="abs section-sub" style="top:1165px">When an unknown printer took a galley of type</div>

<div class="abs card" style="left:113px">
  <svg width="44" height="36" viewBox="0 0 44 36"><path d="M2 32L14 18l8 7L38 6M30 6h8v8M2 34h40" stroke="#dc0b78" fill="none" stroke-width="2"/></svg>
  <h4>Process optimization, digitalization</h4>
  <p>Scrambled it to make a type specimen book. It has survived not only five centuries, but also the leap into electronic</p>
  <span class="rm">READ MORE</span><div class="strip"></div>
</div>
<div class="abs card active" style="left:353px">
  <svg width="56" height="48" viewBox="0 0 56 48"><circle cx="24" cy="24" r="20" stroke="#fff" fill="none" stroke-width="2.5"/><circle cx="24" cy="20" r="5" fill="#fff"/><path d="M15 33c2-6 16-6 18 0" fill="#fff"/><path d="M44 24h10" stroke="#fff" stroke-width="2.5"/></svg>
  <h4>Remote working and productivity</h4>
  <p>Scrambled it to make a type specimen book. It has survived not only five centuries, but also the leap into electronic</p>
  <span class="rm">READ MORE</span>
</div>
<div class="abs card" style="left:594px">
  <svg width="44" height="50" viewBox="0 0 44 50"><circle cx="28" cy="7" r="5" fill="#dc0b78"/><path d="M22 14l10 2-4 12 8 6M24 16l-8 10M4 46h10v-8h10v-8h10" stroke="#dc0b78" fill="none" stroke-width="3"/></svg>
  <h4>Remote leadership</h4>
  <p>Scrambled it to make a type specimen book. It has survived not only five centuries, but also the leap into electronic</p>
  <span class="rm">READ MORE</span><div class="strip"></div>
</div>
<div class="abs card" style="left:830px">
  <svg width="46" height="42" viewBox="0 0 46 42"><rect x="3" y="3" width="40" height="26" fill="#dc0b78"/><path d="M9 22l8-8 6 5 12-10" stroke="#fff" fill="none" stroke-width="2"/><path d="M23 29v8M13 38h20" stroke="#dc0b78" stroke-width="3"/></svg>
  <h4>remote project management</h4>
  <p>Scrambled it to make a type specimen book. It has survived not only five centuries, but also the leap into electronic</p>
  <span class="rm">READ MORE</span><div class="strip"></div>
</div>
<div class="abs card fade" style="left:1071px">
  <svg width="46" height="46" viewBox="0 0 46 46"><circle cx="23" cy="23" r="19" stroke="#dc0b78" fill="none" stroke-width="4" stroke-dasharray="8 4"/><circle cx="23" cy="23" r="8" stroke="#dc0b78" fill="none" stroke-width="3"/></svg>
  <h4>Time management 4. 0</h4>
  <p>Scrambled it to make a type specimen book. It has survived not only five centuries, but also the leap into electronic</p>
  <span class="rm">READ MORE</span><div class="strip"></div>
</div>

<div class="abs section-title" style="top:1732px">What we do</div>
<div class="abs section-sub" style="top:1773px">When an unknown printer took a galley of type</div>

<div class="abs service" style="left:109px">
  <svg width="44" height="50" viewBox="0 0 44 50"><rect x="6" y="6" width="32" height="18" stroke="#dc0b78" fill="none" stroke-width="2"/><path d="M8 30h28l-4 18H12zM22 24v6" stroke="#dc0b78" fill="none" stroke-width="2"/></svg>
  <h5>Keynote Speaking</h5><p>Scrambled it to make a type<br>specimen book. It has survived<br>not only five centuries,</p>
</div>
<div class="abs service" style="left:357px">
  <svg width="50" height="50" viewBox="0 0 50 50"><circle cx="30" cy="10" r="7" stroke="#dc0b78" fill="none" stroke-width="2"/><path d="M18 30c2-10 22-10 24 0M4 32h42M8 32v14M42 32v14M12 40h28" stroke="#dc0b78" fill="none" stroke-width="2"/></svg>
  <h5>Facilitating</h5><p>Scrambled it to make a type<br>specimen book. It has survived<br>not only five centuries,</p>
</div>
<div class="abs service" style="left:611px">
  <svg width="50" height="50" viewBox="0 0 50 50"><rect x="4" y="6" width="42" height="28" stroke="#dc0b78" fill="none" stroke-width="2"/><path d="M12 28v-8M18 28v-12M24 28v-6M25 34l-8 12M25 34l8 12M2 6h46" stroke="#dc0b78" fill="none" stroke-width="2"/><text x="30" y="26" font-family="Poppins,sans-serif" font-size="13" font-weight="700" fill="#dc0b78">$</text></svg>
  <h5>Presentation</h5><p>Scrambled it to make a type<br>specimen book. It has survived<br>not only five centuries,</p>
</div>
<div class="abs service" style="left:859px">
  <svg width="50" height="50" viewBox="0 0 50 50"><rect x="10" y="3" width="30" height="20" stroke="#dc0b78" fill="none" stroke-width="2"/><path d="M15 18l6-6 5 4 8-8" stroke="#dc0b78" fill="none" stroke-width="2"/><circle cx="10" cy="34" r="4" stroke="#dc0b78" fill="none" stroke-width="2"/><circle cx="25" cy="34" r="4" stroke="#dc0b78" fill="none" stroke-width="2"/><circle cx="40" cy="34" r="4" stroke="#dc0b78" fill="none" stroke-width="2"/><path d="M4 47c0-6 12-6 12 0M19 47c0-6 12-6 12 0M34 47c0-6 12-6 12 0" stroke="#dc0b78" fill="none" stroke-width="2"/></svg>
  <h5>Workshops and trainings</h5><p>Scrambled it to make a type<br>specimen book. It has survived<br>not only five centuries,</p>
</div>

<div class="abs pager" style="left:557px;top:2080px"><i></i><i class="on"></i></div>

<div class="abs section-title" style="top:2122px">Our Customers Say Things Like This...</div>
<div class="abs section-sub" style="top:2166px">When an unknown printer took a galley of type</div>

<div class="abs quote dark" style="left:148px">
  <div class="avatar" role="img" aria-label="Client portrait"></div>
  <div class="name">Marten Oska</div><div class="co">BRIGHTLOOP</div>
  <div class="mk">“</div>
  <p>Scrambled it to make a type specimen book. It has survived not only five centuries, but also the leap into electronic typesetting, remaining essentially unchanged. It was popularised in the</p>
</div>
<div class="abs quote pink" style="left:466px">
  <div class="avatar" role="img" aria-label="Client portrait"></div>
  <div class="name">Marten Oska</div><div class="co">BRIGHTLOOP</div>
  <div class="mk">“</div>
  <p>Scrambled it to make a type specimen book. It has survived not only five centuries, but also the leap into electronic typesetting, remaining essentially unchanged. It was popularised in the</p>
</div>
<div class="abs quote" style="left:786px">
  <div class="avatar" role="img" aria-label="Client portrait"></div>
  <div class="name">Marten Oska</div><div class="co">BRIGHTLOOP</div>
  <div class="mk">“</div>
  <p>Scrambled it to make a type specimen book. It has survived not only five centuries, but also the leap into electronic typesetting, remaining essentially unchanged. It was popularised in the</p>
</div>
<div class="abs pager" style="left:542px;top:2666px"><i></i></div>

<div class="abs blog"></div>
<div class="abs section-title" style="top:2806px;color:#fff">Our Latest Blog</div>
<div class="abs section-sub" style="top:2843px;color:#fff">When an unknown printer took a galley of type</div>

<div class="abs post" style="left:143px">
  <div class="ph" role="img" aria-label="Photo of two colleagues reviewing a laptop"><div class="date">31<small>MARCH</small></div></div>
  <h4>Process optimization, digitalization</h4>
  <p>Scrambled it to make a type specimen book. It has survived not only five centuries, but also the leap into electroni</p>
  <div class="rm">READ MORE</div>
</div>
<div class="abs post" style="left:459px">
  <div class="ph" role="img" aria-label="Photo of two colleagues reviewing a laptop"><div class="date">31<small>MARCH</small></div></div>
  <h4>Process optimization, digitalization</h4>
  <p>Scrambled it to make a type specimen book. It has survived not only five centuries, but also the leap into electroni</p>
  <div class="rm">READ MORE</div>
</div>
<div class="abs post" style="left:783px">
  <div class="ph" role="img" aria-label="Photo of two colleagues reviewing a laptop"><div class="date">31<small>MARCH</small></div></div>
  <h4>Process optimization, digitalization</h4>
  <p>Scrambled it to make a type specimen book. It has survived not only five centuries, but also the leap into electroni</p>
  <div class="rm">READ MORE</div>
</div>
<div class="abs" style="left:567px;top:3298px;color:#fff;font-size:10px;font-weight:600;border-bottom:2px solid #fff;padding-bottom:2px">READ MORE</div>

<div class="abs section-title" style="top:3440px">Meet Our Team</div>
<div class="abs section-sub" style="top:3480px">Meet Our Awesome and Creative Team members</div>

<div class="abs member" style="left:117px"><div class="ph" style="background:linear-gradient(#e9eaea,#b7b2ad 70%,#2b2a2c)" role="img" aria-label="Team member portrait"></div><div class="n">Rina Vellmar</div><div class="r">CEO @ Founder</div></div>
<div class="abs member" style="left:364px"><div class="ph" style="background:linear-gradient(#cfd2d3,#8d8682 60%,#1f1d1e)" role="img" aria-label="Team member portrait"></div><div class="n">Rina Vellmar</div><div class="r">CEO @ Founder</div></div>
<div class="abs member" style="left:608px"><div class="ph" style="background:linear-gradient(#4a4d50,#9a8f85 55%,#d5d7d8)" role="img" aria-label="Team member portrait"></div><div class="n">Rina Vellmar</div><div class="r">CEO @ Founder</div></div>
<div class="abs member" style="left:852px"><div class="ph" style="background:linear-gradient(#dfe2e4,#b3b8bc 60%,#44474a)" role="img" aria-label="Team member portrait"></div><div class="n">Rina Vellmar</div><div class="r">CEO @ Founder</div></div>
<div class="abs pager" style="left:557px;top:3944px"><i></i><i class="on"></i></div>

<svg class="abs footer" width="1200" height="600" viewBox="0 0 1200 600">
  <path d="M0 40C180 10 330 110 520 70S820 -20 1000 40 1150 50 1200 30V600H0Z" fill="#dc0b78"/>
  <path d="M0 90C180 60 330 145 540 110S830 30 1000 70 1150 70 1200 80V600H0Z" fill="#1d1a1e"/>
</svg>

<div class="abs news"><div class="ic"><svg width="20" height="20" viewBox="0 0 20 20"><path d="M2 10L18 2 14 18 9 12zM9 12l9-10" stroke="#fff" fill="none" stroke-width="1.5"/></svg></div>Newsletter Subscribe</div>
<div class="abs email">Enter your email id :</div>
<div class="abs sub-btn">SUBSCRIBE</div>

<div class="abs fcol" style="left:113px;width:230px"><h6>ABOUT</h6>Type specimen book. It has survived not only five centuries, but also the leap into electronic typesetting, remaining essentially unchanged. It was popularised in the 1960s with the release of Letraset sheets</div>
<div class="abs fcol" style="left:414px"><h6>Sitemap</h6>Home<br>Service<br>Testimonials<br>Team<br>Blog<br>Contact Us</div>
<div class="abs fcol" style="left:592px"><h6>Services</h6><span class="arr">›</span>Type specimen book. It has<br><span class="arr">›</span>Survived not only five<br><span class="arr">›</span>Centuries, but also the leap<br><span class="arr">›</span>Into electronic typesetting,<br><span class="arr">›</span>Remaining essentially</div>
<div class="abs fcol" style="left:883px;width:200px"><h6>Location</h6><span class="arr">✆</span>Phone:(555)010-7788<br><span class="arr">✉</span>E-mail: info@strideandcalm.example<br><span class="arr">⚲</span>Address:<br><span style="padding-left:18px;display:block;line-height:16px">Marrowfield, 18 Linden Row, 40117</span></div>

<div class="abs rule"></div>
<div class="abs copy">Copyright © 2020 Stride and Calm</div>
<div class="abs follow">Follow us on <i></i><i></i><i></i><i></i></div>

</body>
</html>
```